Business Card Design

hello Guys,
We need a double sided business card. Would like a clean and modern look. Simple, clean, elegant.

Front:
Logo/Company name or Logo/Products
Back:
Contact details

You can go to our website for color scheme.

Information for the business cards are as follows:
Our logo (it is attached)
Products: Divisórias, Forros, Persianas, Pisos
The Company name is: Lumen Painéis
Name: Rodrigo Matheus Valente
Position: Diretor Comercial
Tel: 11 3917-4482 / 95827-6043 / ID: 48*17*26584
Email: contato@lumenpaineis.com.br
Web: www.lumenpaineis.com.br
Address: R: Otávio Brandão 83 – São Paulo – CEP: 04718-230

The card should be of 85mm x 55mm
The winner will deliver:

1) JPG, PNG, TIFF, PDF, Ai, EPS, PSD format files.
The work product will be an Illustrator or Photoshop file
Good luck and let me know if you have any other questions.

CMYK, 300 dpi, convert fonts into paths (vector paths)
set margins at least 4 mm away from the edges

Thanks

```html
<!DOCTYPE html>
<html lang="pt-BR">
<head>
<meta charset="utf-8">
<title>Lumen Painéis – Cartão de Visita</title>
<link href="https://fonts.googleapis.com/css2?family=Montserrat:wght@400;500;700&display=swap" rel="stylesheet">
<style>
  :root {
    --orange: #f47c1c;
    --orange-light: #f99a2e;
    --white: #ffffff;
    --ink: #2a2a2a;
    --grey: #9a9a9a;
    --backdrop: #2f2f2f;
  }
  * { margin: 0; padding: 0; box-sizing: border-box; }
  html, body { width: 1200px; height: 900px; overflow: hidden; }
  body {
    background: var(--backdrop);
    font-family: "Montserrat", sans-serif;
    display: flex;
    align-items: center;
    justify-content: center;
    gap: 40px;
  }
  .card {
    position: relative;
    width: 540px;
    height: 349px;
    border-radius: 14px;
    overflow: hidden;
    background: var(--white);
  }
  .card-shapes { position: absolute; inset: 0; }

  /* Front */
  .brand-block {
    position: absolute;
    left: 120px;
    top: 120px;
    width: 300px;
  }
  .brand-name {
    display: flex;
    align-items: center;
    gap: 12px;
    color: var(--orange);
    font-weight: 700;
    font-size: 32px;
    letter-spacing: 0.3px;
    white-space: nowrap;
  }
  .brand-dot {
    width: 20px; height: 20px;
    border-radius: 50%;
    background: var(--orange);
    flex: none;
  }
  .brand-rule {
    margin-top: 18px;
    height: 2px;
    background: var(--ink);
  }
  .brand-caption {
    margin-top: 10px;
    color: var(--orange);
    font-size: 13px;
    font-weight: 500;
    letter-spacing: 1px;
  }

  /* Back */
  .person {
    position: absolute;
    left: 34px;
    top: 28px;
    display: flex;
    align-items: flex-start;
    gap: 10px;
  }
  .person-icon { width: 24px; height: 24px; flex: none; }
  .person-name { font-size: 18px; font-weight: 700; color: var(--ink); white-space: nowrap; }
  .person-role { font-size: 12px; color: var(--ink); margin-top: 2px; }
  .back-brand {
    position: absolute;
    right: 40px;
    top: 105px;
    color: var(--orange);
    font-weight: 700;
    font-size: 24px;
    white-space: nowrap;
  }
  .contact {
    position: absolute;
    color: var(--white);
    font-size: 11px;
    line-height: 1.5;
    text-align: center;
    white-space: nowrap;
  }
  .contact-phone { left: 39px; top: 142px; width: 150px; }
  .contact-address { left: 136px; top: 172px; width: 200px; }
  .contact-web { left: 316px; top: 205px; width: 180px; }
</style>
</head>
<body>

  <!-- Front side -->
  <section class="card card-front">
    <svg class="card-shapes" viewBox="0 0 540 349" aria-hidden="true">
      <path d="M0,0 L115,0 C55,120 55,230 130,349 L0,349 Z" fill="var(--orange)"/>
      <path d="M440,0 L540,0 L540,349 L455,349 C500,240 505,120 440,0 Z" fill="var(--orange-light)"/>
    </svg>
    <div class="brand-block">
      <div class="brand-name"><span class="brand-dot"></span>Lumen Painéis</div>
      <div class="brand-rule"></div>
      <div class="brand-caption">LUMEN PAINÉIS</div>
    </div>
  </section>

  <!-- Back side -->
  <section class="card card-back">
    <svg class="card-shapes" viewBox="0 0 540 349" aria-hidden="true">
      <path d="M0,120 C150,95 300,215 540,185 L540,349 L0,349 Z" fill="var(--orange)"/>
      <path d="M445,0 L540,0 L540,150 C500,115 470,60 445,0 Z" fill="var(--orange-light)"/>
      <path d="M0,120 C150,95 300,215 540,185" fill="none" stroke="var(--grey)" stroke-width="5"/>
      <!-- phone -->
      <g transform="translate(114,124)">
        <circle r="12" fill="var(--ink)"/>
        <path d="M-5,-6 l3,0 l1,4 l-2,1 a8,8 0 0 0 4,4 l1,-2 l4,1 l0,3 a2,2 0 0 1 -2,2 a13,13 0 0 1 -11,-11 a2,2 0 0 1 2,-2 z" fill="var(--white)"/>
      </g>
      <!-- pin -->
      <g transform="translate(236,154)">
        <circle r="12" fill="var(--ink)"/>
        <path d="M0,8 C-5,2 -6,-1 -6,-3 a6,6 0 0 1 12,0 C6,-1 5,2 0,8 Z" fill="var(--white)"/>
        <circle cy="-3" r="2" fill="var(--ink)"/>
      </g>
      <!-- mail -->
      <g transform="translate(406,187)">
        <circle r="12" fill="var(--ink)"/>
        <rect x="-7" y="-5" width="14" height="10" rx="1" fill="var(--white)"/>
        <path d="M-7,-4 L0,1 L7,-4" fill="none" stroke="var(--ink)" stroke-width="1.3"/>
      </g>
    </svg>

    <div class="person">
      <svg class="person-icon" viewBox="0 0 24 24" aria-hidden="true">
        <circle cx="12" cy="12" r="12" fill="var(--ink)"/>
        <circle cx="12" cy="9" r="3.5" fill="var(--white)"/>
        <path d="M5.5,19 a6.5,5 0 0 1 13,0 z" fill="var(--white)"/>
      </svg>
      <div>
        <div class="person-name">Rodrigo Matheus Valente</div>
        <div class="person-role">Diretor Comercial</div>
      </div>
    </div>

    <div class="back-brand">Lumen Painéis</div>

    <div class="contact contact-phone">11 3917-4482<br>95827-6043</div>
    <div class="contact contact-address">R: Otávio Brandão 83, São Paulo<br>CEP: 04718-230</div>
    <div class="contact contact-web">contato@lumenpaineis.com.br<br>www.lumenpaineis.com.br</div>
  </section>

</body>
</html>
```